Flyer Design Project

I need a cool design that describes a new line of services I am selling. The final product should be a 8 1/2 by 11 and maximum two pages.

I am selling consulting services to learn to use web conferencing tools for business development, meeting and training.

Please use the file I have attached as a guide for your work. It is a document called "primer-thriftyhacksguide" and I love its design.

Thanks

                                        Please substitute the new text availble and just uploaded in the FLYER. Please submit the FINAL version fo your design with TExt changes as well as improvements detailed in previous message. 

Target Market(s)

Entrepreneurs and classroom educators who wnats to explore a new way to teach (innovators not scared of technology)

Industry/Entity Type

Business

Requirements
Must have
• I would like to receive a final PDF with the content EDITABLE for minor edits (I have acrobat)
Logo should be included (attached)

PLEASE CHECK OUT ATTACHED DOCUMENT WHOSE DESIGN I LOVE.
IT is called "Primer thrifty-hacks guide". If you could follow that as a template to design mine that would be great!

```html
<!DOCTYPE html>
<html lang="en">
<head>
<meta charset="utf-8">
<title>Online Meeting Skills Services – Flyer</title>
<link rel="stylesheet" href="https://fonts.googleapis.com/css2?family=Arimo:wght@400;700&family=Roboto+Condensed:wght@700&display=swap">
<style>
  :root{
    --stage:#cfcac4;
    --paper:#ffffff;
    --ink:#222222;
    --blue:#1f4e9c;
    --blue-soft:#dbe6f5;
    --blue-line:#5d86c9;
    --orange:#e07b1a;
    --red:#c8282d;
  }
  *{box-sizing:border-box;margin:0;padding:0}
  html,body{width:1200px;height:900px;overflow:hidden}
  body{background:var(--stage);font-family:"Arimo",Arial,sans-serif;color:var(--ink);position:relative}

  .page{position:absolute;top:225px;width:580px;height:450px;background:var(--paper);overflow:hidden;box-shadow:0 4px 14px rgba(0,0,0,.25)}
  .page--intro{left:14px}
  .page--services{left:606px}

  .swirl{position:absolute;pointer-events:none}
  .page--intro .swirl--top{left:0;top:0;width:230px;height:150px;background:radial-gradient(ellipse at 0 0,#b9cdea 0%,rgba(185,205,234,0) 70%)}
  .page--intro .swirl--bottom{right:0;bottom:0;width:300px;height:160px;background:radial-gradient(ellipse at 100% 100%,#c3d4ee 0%,rgba(195,212,238,0) 70%)}

  .intro-title{position:relative;font-family:"Roboto Condensed","Arial Narrow",sans-serif;font-size:19px;letter-spacing:.1px;margin:22px 20px 8px;color:#111}
  .intro-lead{position:relative;margin:0 18px;padding:8px 10px;border-top:2px solid var(--blue-line);border-bottom:1px solid var(--blue-line);background:rgba(219,230,245,.55)}
  .intro-lead h2{font-size:12px;color:var(--orange);font-weight:700;line-height:1.25}
  .intro-lead p{font-size:10px;color:var(--blue);font-weight:700;line-height:1.25;margin-top:2px}
  .intro-body{position:relative;margin:12px 28px 0;font-size:9.6px;line-height:1.42}
  .intro-body p{margin-bottom:9px}
  .intro-list{list-style:none;margin-left:12px}
  .intro-list li{position:relative;padding-left:14px;margin-bottom:9px}
  .intro-list li::before{content:"";position:absolute;left:0;top:4px;width:5px;height:5px;border-radius:50%;background:var(--ink)}

  .page--services{background:linear-gradient(160deg,#ffffff 0%,#eef3fb 55%,#dfe9f7 100%)}
  .page--services .swirl--wash{inset:0;background:radial-gradient(ellipse at 20% 30%,rgba(170,195,232,.45),rgba(170,195,232,0) 60%)}
  .services-title{position:relative;font-size:19px;font-weight:700;margin:16px 18px 2px;color:#111;letter-spacing:-.2px}
  .services-sub{position:relative;font-size:11px;color:var(--orange);font-weight:700;font-style:italic;margin:0 0 8px 128px}

  .service-grid{position:absolute;left:14px;top:62px;width:552px;height:376px;display:grid;grid-template-columns:repeat(4,1fr) 112px;grid-template-rows:205px 1fr;gap:6px}
  .service{background:var(--paper);border:1.5px solid var(--blue-line);padding:6px;display:flex;flex-direction:column;font-size:7.2px;line-height:1.3}
  .service strong{color:var(--blue)}
  .service .price{margin-top:auto;align-self:flex-end;color:var(--red);font-weight:700;font-size:9px}

  .contact{grid-column:5;grid-row:1 / span 2;display:flex;flex-direction:column;justify-content:flex-end;padding:0 2px 4px}
  .contact-note{font-size:8.6px;font-weight:700;color:var(--blue);line-height:1.3;margin-bottom:12px}
  .contact-more{font-size:12.5px;font-weight:700;color:var(--blue)}
  .contact-call{font-size:8px;color:var(--blue);margin-left:26px}
  .contact-phone{font-size:15px;font-weight:700;color:var(--red);margin-bottom:12px}
  .brand-name{font-size:12px;font-weight:700;color:var(--blue);text-align:right}
  .brand-tag{font-size:7px;color:var(--blue);text-align:right;margin-top:2px}
  .service-grid .bottom{grid-row:2}
</style>
</head>
<body>

<section class="page page--intro">
  <div class="swirl swirl--top" role="img" aria-label="Soft blue abstract swirl decoration"></div>
  <div class="swirl swirl--bottom" role="img" aria-label="Soft blue abstract swirl decoration"></div>

  <h1 class="intro-title">ONLINE MEETING SKILLS SERVICES: It is just the beginning...</h1>

  <div class="intro-lead">
    <h2>What if your business can reach all the people already interested in learning what you know?</h2>
    <p>A different use of webinar technology: the first step towards a new way of thinking about your markets/your clients.</p>
  </div>

  <div class="intro-body">
    <p>You probably know about webinars. You may have attended a few yourself. Perhaps you found them boring and un-engaging, with no chance to interact or ask questions to a guarded speaker. Did the speaker drone on as you – yes, you! – checked your email? Good news: we are not talking about "that" kind of webinars. Yes there is another way!</p>
    <p>Turn your expertise into engaging and interactive online sessions delivered "live": Engage people online in conversations that matter to them and forget about the technical details. We take care of selecting the right webinar technology and we provide the training that fits your goals. Convergence offers you all you need to break into online learning:</p>
    <ul class="intro-list">
      <li>We design an effective virtual session that helps your audience reach their full potential through a different, more engaging level of interactivity.</li>
      <li>We repurpose your marketing materials and content for online learning.</li>
      <li>We develop and execute a communication plan to reach your list – already interested in learning what you know.</li>
      <li>We support you "hands-on" at your first live event inside your virtual training room. We orchestrate the tools and activities you need to engage your remote participants.</li>
    </ul>
  </div>
</section>

<section class="page page--services">
  <div class="swirl swirl--wash" role="img" aria-label="Light blue abstract swirl background"></div>

  <h1 class="services-title">Choose the service that best fit your needs and budget:</h1>
  <p class="services-sub">A new level of online engagement and virtual collaboration awaits.</p>

  <div class="service-grid">
    <article class="service"><p><strong>Webinar Series:</strong> Plan, design, develop and implement a 3+1 online webinar series about the content of your expertise marketed to live audiences with 3 hours of One-on-One online coaching on web conferencing tools and how to use them for your business. Includes access to online resource library of our Online Facilitator Certification plus access to your own online meeting room and virtual collaboration platform.</p><span class="price">$3,000</span></article>
    <article class="service"><p><strong>Webinar:</strong> Plan, design, develop and implement 1 webinar session on the content of your expertise marketed to live audiences with 3 hours of One-on-One online coaching on web conferencing tools and how to use them for your business. Includes access to online resource library of our Online Facilitator Certification plus access to your own online meeting room and virtual collaboration platform.</p><span class="price">$1,900</span></article>
    <article class="service"><p><strong>Outfitting the Online Entrepreneur:</strong> 6 hours of One-on-One online coaching to learn about web conferencing tools and how to use them for your business. Includes access to online resource library of our Online Facilitator Certification plus access to your own online meeting room and virtual collaboration platform.</p><span class="price">$1,300</span></article>
    <article class="service"><p><strong>Outfitting the Online Educator:</strong> 3 hours of One-on-One online coaching to learn about web conferencing tools and how to use them for your training. Includes access to online resource library of our Online Facilitator Certification plus access to your own online meeting room and virtual collaboration platform.</p><span class="price">$1,200</span></article>

    <aside class="contact">
      <p class="contact-note">You'll participate via the Confera Live Meeting platform. No special software is required. If you have a computer with Internet access and a direct telephone line you have all is needed to participate.</p>
      <p class="contact-more">Want to know more?</p>
      <p class="contact-call">Call us at:</p>
      <p class="contact-phone">555-0142-3380</p>
      <p class="brand-name">Convergence</p>
      <p class="brand-tag">Learning. Teamwork. Growth.</p>
    </aside>

    <article class="service bottom"><p><strong>Repurposing for Online Audiences:</strong> Design and develop materials, agenda, event plan and activities to repurpose your face-to-face session for online sessions that market your expertise. Includes 3 hours of One-on-One online coaching to learn about web conferencing tools and how to use them for your business.</p><span class="price">$500</span></article>
    <article class="service bottom"><p><strong>One-on-one coaching with resources:</strong> 2 hours of One-on-One online coaching to learn about web conferencing tools and how to use them for your business. Includes access to online resource library of our Online Facilitator Certification.</p><span class="price">$300</span></article>
    <article class="service bottom"><p><strong>One-on-one coaching:</strong> 2 hours of One-on-One online coaching to learn about web conferencing tools and how to use them for your business. Includes three job aids for online facilitation.</p><span class="price">$200</span></article>
  </div>
</section>

</body>
</html>
```